International Container Business Company Needs a Letterhead Design

We need a letterhead design for our company in Hamburg / Germany ( located in the Port ) called RV Kontor GmbH -

www.rv-kontor.de

We have our own logo , please use this one -
We would like to see designs that use the color blue.

RV Kontor GmbH is a young, dynamic and successful company in the container industry.

Our activities cover the following areas:
Container Trade
Container Rental
Container Transport
Maintenance and repair of refrigerated containers
Reefer Service and 24 hour emergency service
Pre Trip Inspection (PTI)
Storage and shipping containers repairs
Depot and terminal service

Industry/Entity Type

Business

Colors
3176b5
0455a3

Requirements
Must have
• The company is acutally called Belsket Handel,
• but we are changing the companies name to
• RV Kontor GmbH ,
• the website will be : www.rv-kontor.de
• and the email is : info@rv-kontor.de
• the rest still same as on the webpage
• thanks

```html
<!DOCTYPE html>
<html lang="de">
<head>
<meta charset="utf-8">
<title>RV Kontor GmbH – Briefbogen</title>
<link href="https://fonts.googleapis.com/css2?family=Source+Sans+3:wght@400;600&display=swap" rel="stylesheet">
<style>
  :root {
    --paper: #ffffff;
    --brand-blue: #2d3b93;
    --text-light: #ffffff;
  }
  html, body {
    margin: 0;
    padding: 0;
    overflow: hidden;
    background: var(--paper);
  }
  .letterhead {
    position: relative;
    width: 849px;
    height: 1200px;
    background: var(--paper);
    overflow: hidden;
    font-family: "Source Sans 3", sans-serif;
  }
  .brand {
    position: absolute;
    top: 96px;
    left: 0;
    width: 100%;
    display: flex;
    justify-content: center;
    align-items: center;
    gap: 14px;
  }
  .brand-dot {
    width: 30px;
    height: 30px;
    border-radius: 50%;
    background: var(--brand-blue);
  }
  .brand-name {
    font-size: 34px;
    font-weight: 600;
    color: var(--brand-blue);
    letter-spacing: 0.5px;
  }
  .contact-disc {
    position: absolute;
    left: 50%;
    top: 1013px;
    width: 402px;
    height: 402px;
    margin-left: -201px;
    border-radius: 50%;
    background: var(--brand-blue);
  }
  .contact {
    position: absolute;
    left: 0;
    top: 1064px;
    width: 100%;
    text-align: center;
    color: var(--text-light);
    font-size: 18px;
    line-height: 24.5px;
  }
  .contact p { margin: 0; }
</style>
</head>
<body>
  <div class="letterhead">
    <header class="brand">
      <span class="brand-dot"></span>
      <span class="brand-name">RV Kontor GmbH</span>
    </header>

    <footer>
      <div class="contact-disc"></div>
      <address class="contact" style="font-style: normal;">
        <p>Address Line 01, Adress Line 02.</p>
        <p>T 888 5555 555</p>
        <p>F 888 5555 555</p>
        <p>E info@rv-kontor.de</p>
        <p>www.rv-kontor.de</p>
      </address>
    </footer>
  </div>
</body>
</html>
```